New modern business card design

To design a brand new business card that's clean & modern in terms of layout.
I have attached our company logo and also basic information regarding what is needed on the card that also needs to be editable.

Target Market(s)

motor trade

Contact Information for Business Card

logo, name, title, tel, mob, email, address, www, all information is in the word.doc file

Requirements
Must have
• white background
Nice to have
• Nice clean font

```html
<!DOCTYPE html>
<html lang="en">
<head>
<meta charset="utf-8">
<title>Bolt Recovery Ltd – Business Cards</title>
<link href="https://fonts.googleapis.com/css2?family=Michroma&family=Open+Sans:wght@400;600&display=swap" rel="stylesheet">
<style>
  :root {
    --backdrop: #e4e6e9;
    --card: #ffffff;
    --pattern-top: #eef0f3;
    --pattern-bottom: #ffffff;
    --blue: #1f7fd6;
    --text: #3a3d42;
    --rule: #c8ccd2;
  }
  * { margin: 0; padding: 0; box-sizing: border-box; }
  html, body {
    width: 1200px; height: 1108px; overflow: hidden;
    background: var(--backdrop);
  }
  .stage {
    position: relative; width: 1200px; height: 1108px;
    display: flex; justify-content: center; align-items: center; gap: 60px;
  }
  .card {
    width: 420px; height: 680px; border-radius: 26px;
    background: var(--card);
    box-shadow: 0 14px 34px rgba(0,0,0,.18);
    position: relative; overflow: hidden;
    font-family: "Open Sans", sans-serif; color: var(--text);
    text-align: center;
  }
  .brand {
    display: flex; align-items: center; justify-content: center; gap: 12px;
    font-family: "Michroma", sans-serif; color: var(--blue);
    font-size: 22px; letter-spacing: 1px; white-space: nowrap;
  }
  .brand-square { width: 18px; height: 18px; background: var(--blue); flex: none; }
  .front .brand { margin-top: 140px; }
  .brand-rule { width: 300px; height: 1px; background: var(--blue); margin: 18px auto 0; }
  .person-name {
    font-family: "Michroma", sans-serif; color: var(--blue);
    font-size: 26px; font-weight: 400; margin-top: 50px; letter-spacing: 1px;
  }
  .person-title { font-size: 17px; margin-top: 6px; }
  .divider { width: 230px; height: 1px; background: var(--rule); margin: 14px auto; }
  .address { font-size: 17px; line-height: 1.35; }
  .web { color: var(--blue); font-size: 17px; margin-top: 4px; }
  .contact { font-size: 17px; line-height: 1.4; }
  .contact .label { color: var(--blue); font-weight: 600; margin-right: 4px; }
  .back-pattern {
    position: absolute; left: 0; top: 0; width: 100%; height: 440px;
    background: linear-gradient(160deg, var(--pattern-top), var(--pattern-bottom));
  }
  .back-brand { position: absolute; left: 0; right: 0; top: 480px; }
  .back-brand .brand-rule { width: 320px; }
  .back-web { font-size: 17px; margin-top: 26px; }
</style>
</head>
<body>
<main class="stage">
  <section class="card front">
    <div class="brand"><span class="brand-square"></span>BOLT RECOVERY LTD</div>
    <div class="brand-rule"></div>
    <h1 class="person-name">DANIEL MORRIS</h1>
    <p class="person-title">General Manager</p>
    <div class="divider"></div>
    <p class="address">Carlton Road<br>Denford, Ashbury<br>AB12 3CD</p>
    <p class="web">www.bolt-recovery.co.uk</p>
    <div class="divider"></div>
    <p class="contact"><span class="label">P:</span>0161 555 0182<br>
      <span class="label">M:</span>07700 900 415<br>
      <span class="label">E:</span>dmorris@bolt-recovery.co.uk</p>
  </section>

  <section class="card back">
    <div class="back-pattern" role="img" aria-label="Faint repeated brand-mark pattern"></div>
    <div class="back-brand">
      <div class="brand"><span class="brand-square"></span>BOLT RECOVERY LTD</div>
      <div class="brand-rule"></div>
      <p class="back-web">www.bolt-recovery.co.uk</p>
    </div>
  </section>
</main>
</body>
</html>
```